Walk Bold Stay Kind Ebook and Print book cover

I need a professional, eye catching cover that will stand out. The title of the book is "Walk Bold Stay Kind: 47 Quiet Rules For Calm and Wonder" It is a self-help personal transformation book by author Dale Ormsby. The cover will be on both print and ebook covers. I want something that is similar yet different to best-selling books in the genre, nothing too boring. A blue background might work, but it isn't a requirement. I'm open to other colors as long as it's powerful, professional, and screams "Buy me because this book is going to change your life!"
Updates

So far, 3 designs (3 of the 4 star rated designs) are in contention, but they all can be improved. I think the book cover should best convey "thinking smart" in a dynamic way. I'll run another poll in a day or so when I get additional designs I like. Added Thursday, May 4, 2017

Based on current designs, I wanted to provide additional guidance. The title and image should pop and be clearly visible at a distance as a thumbnail. Also, I'm wanting something bold and creative but not too confusing. I currently have a couple solid designs that are in contention to win, but I have another 7 days left for the project. I extended it to 10 days from the initial 5. I'll include several more polls for my followers and will likely pick the top ranking design based off the series of polls and will be eliminating lower ranking designs with each new poll and set of promising designs that come in. Finally, I may ask to see what the back will look like on the print version since I'll need both the Lumora and print (5" by 8") designs. Added Saturday, May 6, 2017

It's been recommended by some that I should have my own picture on the cover. I'm not completely convinced, but I would like to see some additional designs that incorporate my photo (touched up to remove the shine from my forehead and the label brand name removed from the t-shire) into a cover design. I have several good designs coming in, so typeset and professional looking font is extremely important. Blue is also preferred but not required. I've attached the photo on the brief for those who want to submit a design with that photo. Added Saturday, May 6, 2017

Target Market(s)

Working age adults seeking personal transformation and self improvement.

Industry/Entity Type

Motivation

Requirements
Must have
• Creativity. Eye catching. Striking. Contrast. Looks good close up and as a thumbnail at a distance. Font should be easy to read and pop from the cover along with the design.
Nice to have
• Powerful image placement. Play up the "Walk Bold" aspect of the title. Perhaps even contrasting someone who's thinking "Hard." Here are a few examples of intriguing covers (though not necessarily related to the genre) I like mainly for aesthetics and creativity. https://www.shopvale.com/dp/Q71MRT2KWD/ https://www.shopvale.com/dp/Q34PLN8XEA
• https://www.shopvale.com/dp/Q925GHV3TC/
• https://www.shopvale.com/dp/Q48DJW6RZB/
• (the font is a little poor in the last one but the image is evoking)
Should not have
• Ugly, tacky, or hard to read fonts. A simple photo with text on top. A simple background with words. Confusing images. Designs with no additional stock image purchase requirements will be given preference over those that do. I've seen a lot of balloons and light bulbs. I'm not saying you can't include them in the design, but if you want to stand out, try to find something more creative that expresses the concept of the title.

```html
<!DOCTYPE html>
<html lang="en">
<head>
<meta charset="utf-8">
<title>Walk Bold Stay Kind — Dale Ormsby</title>
<link rel="stylesheet" href="https://fonts.googleapis.com/css2?family=EB+Garamond:wght@400;500&display=swap">
<style>
  :root {
    --page: #ffffff;
    --navy: #04013f;
    --navy-deep: #020030;
    --dot-grey: #4d4d55;
    --glow: #b8b04a;
    --ink: #ffffff;
  }
  * { margin: 0; padding: 0; box-sizing: border-box; }
  html, body {
    width: 1200px;
    height: 1200px;
    overflow: hidden;
    background: var(--page);
  }
  .cover {
    position: absolute;
    left: 242px;
    top: 30px;
    width: 712px;
    height: 1140px;
    background: var(--navy);
    overflow: hidden;
    font-family: "EB Garamond", Georgia, serif;
    color: var(--ink);
  }
  .dot-field {
    position: absolute;
    left: 0;
    top: 430px;
    width: 700px;
    height: 710px;
    background:
      linear-gradient(90deg, rgba(77,77,85,0.95) 0%, rgba(77,77,85,0.85) 40%, rgba(77,77,85,0.45) 75%, rgba(77,77,85,0) 100%);
    -webkit-mask-image: linear-gradient(180deg, rgba(0,0,0,0.6) 0%, #000 25%, #000 100%);
    mask-image: linear-gradient(180deg, rgba(0,0,0,0.6) 0%, #000 25%, #000 100%);
  }
  .brain-art {
    position: absolute;
    left: 122px;
    top: 18px;
    width: 376px;
    height: 400px;
    background:
      radial-gradient(ellipse 55% 30% at 50% 22%, rgba(220,210,90,0.55) 0%, rgba(184,176,74,0.25) 50%, rgba(184,176,74,0) 100%),
      radial-gradient(ellipse 50% 48% at 50% 42%, rgba(120,115,60,0.45) 0%, rgba(120,115,60,0.15) 70%, rgba(120,115,60,0) 100%);
    border-radius: 48% 48% 40% 40%;
  }
  .title { font-weight: 400; }
  .title-line {
    position: absolute;
    display: block;
    line-height: 1;
    font-weight: 400;
    white-space: nowrap;
    text-shadow: 0 2px 6px rgba(0,0,0,0.35);
  }
  .title-line--first { left: 188px; top: 362px; font-size: 200px; letter-spacing: -1px; }
  .title-line--second { left: 54px; top: 511px; font-size: 200px; letter-spacing: -1px; }
  .title-line--third { left: 160px; top: 682px; font-size: 100px; }
  .subtitle {
    position: absolute;
    left: 0;
    width: 712px;
    top: 852px;
    padding-left: 6px;
    text-align: center;
    font-size: 29px;
    line-height: 34px;
  }
  .author {
    position: absolute;
    right: 32px;
    top: 1070px;
    font-size: 31px;
    letter-spacing: 0.5px;
    text-transform: uppercase;
  }
</style>
</head>
<body>
  <main class="cover">
    <div class="dot-field" role="img" aria-label="Grid of small grey dots fading from left to right"></div>
    <div class="brain-art" role="img" aria-label="Dotted golden brain illustration with glowing constellation lines across the top"></div>
    <h1 class="title">
      <span class="title-line title-line--first">Walk</span>
      <span class="title-line title-line--second">Bold</span>
      <span class="title-line title-line--third">Stay Kind</span>
    </h1>
    <p class="subtitle">47 Quiet Rules<br>For Calm and Wonder</p>
    <p class="author">Dale Ormsby</p>
  </main>
</body>
</html>
```